Industrial Automation company requires a business card design

Valtrin Automation provides design & build of Automated Equipment for manufacturing industry.
www.valtrinautomation.example
The equipment we design is used for manufacturing in sectors such as medical device, pharmaceutical, aerospace and electronics.
We require a new business card design which incorporates our (New) logo and the key message words:
Automated Equipment:
Design, Build, Control, Test, Support

```html
<!DOCTYPE html>
<html lang="en">
<head>
<meta charset="utf-8">
<title>Valtrin Automation — Business Card</title>
<link rel="stylesheet" href="https://fonts.googleapis.com/css2?family=Montserrat:wght@400;600;700&display=swap">
<style>
  :root {
    --stage: #1e1e1e;
    --card: #ffffff;
    --brand-green: #8dc63f;
    --ink: #231f20;
    --muted-ink: #4a4748;
    --gear-grey: #dcdbdc;
    --gear-green: #e9f2dc;
  }
  * { margin: 0; padding: 0; box-sizing: border-box; }
  html, body {
    width: 1200px; height: 1200px; overflow: hidden;
    background: var(--stage);
    font-family: "Montserrat", "Century Gothic", sans-serif;
    color: var(--ink);
  }
  .canvas { position: relative; width: 1200px; height: 1200px; }

  .card { position: absolute; background: var(--card); overflow: hidden; }

  /* Front face */
  .card--front { left: 186px; top: 97px; width: 828px; height: 471px; }
  .card--front .base-band {
    position: absolute; left: 3px; right: 0; bottom: 0; height: 29px;
    background: var(--brand-green);
  }
  .gear-panel {
    position: absolute; left: 0; top: 20px; width: 292px; height: 218px;
    background: linear-gradient(135deg, var(--gear-grey) 0%, #e8e7e8 55%, var(--gear-green) 100%);
    border-radius: 0 14px 14px 0;
  }

  .wordmark {
    position: absolute; display: flex; align-items: center;
    font-weight: 700; color: var(--brand-green);
    text-transform: uppercase; white-space: nowrap;
  }
  .wordmark__dot { border-radius: 50%; background: var(--ink); flex: none; }
  .card--front .wordmark { left: 186px; top: 211px; font-size: 32px; letter-spacing: 0.8px; gap: 14px; }
  .card--front .wordmark__dot { width: 44px; height: 44px; }

  .key-message {
    position: absolute; left: 244px; top: 272px;
    font-size: 12px; font-weight: 600; letter-spacing: 1.2px;
    text-transform: uppercase; color: var(--muted-ink); white-space: nowrap;
  }
  .key-message__lead { color: var(--brand-green); }

  /* Back face */
  .card--back { left: 188px; top: 645px; width: 825px; height: 472px; }
  .side-band { position: absolute; top: 0; bottom: 0; background: var(--brand-green); }
  .side-band--left { left: 0; width: 26px; }
  .side-band--right { right: 0; width: 25px; }
  .card--back .wordmark { left: 65px; top: 215px; font-size: 23px; letter-spacing: 0.5px; gap: 11px; }
  .card--back .wordmark__dot { width: 34px; height: 34px; }

  .person { position: absolute; left: 489px; top: 84px; }
  .person__name { font-size: 24px; font-weight: 700; letter-spacing: 0.3px; }
  .person__role { font-size: 17px; margin-top: 2px; margin-left: -4px; }

  .contact { position: absolute; left: 476px; top: 210px; list-style: none; font-size: 19.5px; }
  .contact__item { display: flex; align-items: flex-start; line-height: 24px; }
  .contact__icon { width: 40px; flex: none; display: flex; justify-content: flex-start; padding-top: 2px; }
  .contact__icon svg { fill: var(--ink); }
  .contact__item--phone { margin-bottom: 28px; }
  .contact__item--address { margin-bottom: 20px; }
  .contact__item--web { margin-bottom: 12px; }
</style>
</head>
<body>
<main class="canvas">

  <section class="card card--front" aria-label="Card front">
    <div class="gear-panel" role="img" aria-label="Decorative group of grey and green machine gears"></div>
    <div class="wordmark"><span class="wordmark__dot"></span>Valtrin Automation</div>
    <p class="key-message"><span class="key-message__lead">Automated Equipment:</span> Design · Build · Control · Test · Support</p>
    <div class="base-band"></div>
  </section>

  <section class="card card--back" aria-label="Card back">
    <div class="side-band side-band--left"></div>
    <div class="side-band side-band--right"></div>

    <div class="wordmark"><span class="wordmark__dot"></span>Valtrin Automation</div>

    <div class="person">
      <p class="person__name">PLACE NAME</p>
      <p class="person__role">(Position)</p>
    </div>

    <ul class="contact">
      <li class="contact__item contact__item--phone">
        <span class="contact__icon">
          <svg width="20" height="20" viewBox="0 0 24 24" aria-hidden="true"><path d="M6.6 10.8a15.1 15.1 0 0 0 6.6 6.6l2.2-2.2a1 1 0 0 1 1-.25 11.4 11.4 0 0 0 3.6.57 1 1 0 0 1 1 1V20a1 1 0 0 1-1 1A17 17 0 0 1 3 4a1 1 0 0 1 1-1h3.5a1 1 0 0 1 1 1c0 1.25.2 2.45.57 3.57a1 1 0 0 1-.25 1z"/></svg>
        </span>
        <span>+91 9000 414 141<br>+91 9000 525 252</span>
      </li>
      <li class="contact__item contact__item--address">
        <span class="contact__icon">
          <svg width="23" height="20" viewBox="0 0 24 22" aria-hidden="true"><path d="M12 1 0 11h3v10h6v-7h6v7h6V11h3z"/></svg>
        </span>
        <span>Place Your office address</span>
      </li>
      <li class="contact__item contact__item--web">
        <span class="contact__icon">
          <svg width="22" height="22" viewBox="0 0 24 24" aria-hidden="true"><circle cx="12" cy="12" r="11"/><path d="M8 5c2 1 1 3 3 3s1 3-1 3-3 2-2 4-2 2-3 0M15 14c2-1 4 0 4 2s-2 3-3 3-2-3-1-5z" fill="#fff"/></svg>
        </span>
        <span>Place Your website</span>
      </li>
      <li class="contact__item contact__item--email">
        <span class="contact__icon">
          <svg width="23" height="16" viewBox="0 0 24 16" aria-hidden="true" style="margin-top:4px"><path d="M0 0h24v16H0z"/><path d="M1 1l11 8 11-8" fill="none" stroke="#fff" stroke-width="1.6"/></svg>
        </span>
        <span>Place Your Email address</span>
      </li>
    </ul>
  </section>

</main>
</body>
</html>
```